Sam Greenfield Billboard

**Task Description: Billboard Design for Self Storage Facility**

**Objective:**
Design a captivating billboard to promote our self-storage facility with a focus on our convenient location and online rental capabilities.

**Key Messages to Include:**
1. **Location Emphasis:** Highlight that our facility is located right beside the billboard (maybe by using an arrow pointing left).
2. **Online Rental Convenience:** Feature prominently that customers can "Rent Online Anytime!” or that we are "Always Open Online!"

**Target Audience:**
- Local residents looking for convenient self-storage solutions.
- Businesses needing storage space accessible around the clock.

**Design Elements:**
1. **Visual Impact:** Eye-catching graphics and colors that stand out against the surroundings.
2. **Clear Text:** Bold and concise messaging that can be read and understood quickly.
3. **Contact Information:** Include our phone number and website URL for easy access to further information.

**Additional Information:**
- Billboard dimensions: 12 ft. x 24 ft.
- Preferred color scheme: Bright and attention-grabbing, but professional.
- Branding: Incorporate our logo and brand colors to maintain consistency.

**Deliverables:**
- High-resolution digital file compatible with billboard printing specifications.
- Consider mockups or visualizations for presentation purposes.

Please note that I have attached current logos/graphics that we would love to incorporate into the billboard as well as a picture of our current billboard. Our logo (Sam Greenfield Self Storage - SG navy.png) MUST be incorporated into the billboard. Also feel free to add any of the current descriptions from the picture of our current billboard into the design. Instead of using "Climate Controlled" use "Temperature Controlled". Thank you for your attention to these details. We look forward to reviewing your proposed design!

```html
<!DOCTYPE html>
<html lang="en">
<head>
<meta charset="utf-8">
<title>Sam Greenfield Billboard</title>
<link rel="stylesheet" href="https://fonts.googleapis.com/css2?family=Anton&family=Poppins:wght@500;600;700&display=swap">
<style>
:root{
  --page:#dcdbdc;
  --paper:#ffffff;
  --navy:#0b2361;
  --bronze:#9a7654;
  --ink:#1c1c1c;
}
*{margin:0;padding:0;box-sizing:border-box}
html,body{width:965px;height:1200px;overflow:hidden;background:var(--page)}
.billboard{position:absolute;left:32px;top:375px;width:900px;height:450px;background:var(--paper);overflow:hidden;box-shadow:0 4px 14px rgba(0,0,0,.18)}
.art{position:absolute;left:0;top:0;width:900px;height:450px}
.brand{position:absolute;left:160px;top:24px;width:220px;text-align:center;color:var(--navy);font-family:"Poppins",sans-serif}
.brand-name{display:block;font-weight:700;font-size:26px;line-height:30px;letter-spacing:.5px;text-transform:uppercase}
.brand-sub{display:block;font-weight:600;font-size:12px;letter-spacing:7px;line-height:18px;text-transform:uppercase}
.headline{position:absolute;left:36px;top:92px;font-family:"Anton",sans-serif;font-size:84px;line-height:92px;letter-spacing:.5px;white-space:nowrap}
.headline .self{color:var(--bronze)}
.headline .storage{color:var(--navy)}
.tagline{position:absolute;left:37px;top:180px;font-family:"Poppins",sans-serif;font-weight:600;font-size:36px;line-height:40px;letter-spacing:1.6px;color:var(--ink);white-space:nowrap}
.features{position:absolute;left:37px;top:228px;display:flex;gap:12px;font-family:"Poppins",sans-serif;font-weight:600;font-size:15px;line-height:17px;color:var(--ink)}
.feature{display:flex;align-items:center;gap:6px}
.feature svg{width:34px;height:34px;flex:none}
.address{position:absolute;left:175px;top:290px;width:680px;height:56px;font-family:"Poppins",sans-serif;font-weight:600;font-size:48px;line-height:56px;letter-spacing:1px;color:#fff;text-align:center;white-space:nowrap}
.contact{position:absolute;left:0;top:362px;width:900px;height:88px;display:flex;align-items:center;justify-content:center;gap:22px;font-family:"Poppins",sans-serif;font-weight:600;font-size:31px;color:#fff;padding-bottom:6px}
.contact span{display:flex;align-items:center;gap:8px}
.contact svg{width:26px;height:26px}
</style>
</head>
<body>
<main class="billboard">
  <svg class="art" viewBox="0 0 900 450" aria-hidden="false">
    <defs>
      <linearGradient id="sky" x1="0" y1="0" x2="0" y2="1">
        <stop offset="0" stop-color="#5d8fd0"/>
        <stop offset=".32" stop-color="#a9c3e0"/>
        <stop offset=".36" stop-color="#7d8580"/>
        <stop offset=".7" stop-color="#3c4148"/>
        <stop offset="1" stop-color="#545a60"/>
      </linearGradient>
      <linearGradient id="screen" x1="0" y1="0" x2="0" y2="1">
        <stop offset="0" stop-color="#e9edf3"/>
        <stop offset=".15" stop-color="#5b5f66"/>
        <stop offset=".75" stop-color="#3a3e46"/>
        <stop offset=".76" stop-color="#ffffff"/>
      </linearGradient>
    </defs>
    <path class="swoosh-bronze" d="M522,0H900V240C820,282 700,292 640,252C560,202 505,80 522,0Z" fill="var(--bronze)"/>
    <path class="swoosh-navy" d="M532,0H900V226C820,266 710,272 650,236C575,190 520,80 532,0Z" fill="var(--navy)"/>
    <path class="facility-photo" role="img" aria-label="Photo of the storage facility: rows of units with dark roll-up doors under a blue sky" d="M545,0H900V202C820,236 720,244 662,214C592,176 535,80 545,0Z" fill="url(#sky)"/>
    <g class="devices" role="img" aria-label="Tablet and phone showing the online rental website">
      <rect x="633" y="114" width="198" height="154" rx="8" fill="#1a1a1e"/>
      <rect x="639" y="120" width="186" height="142" rx="3" fill="url(#screen)"/>
      <rect x="826" y="171" width="38" height="100" rx="6" fill="#1a1a1e"/>
      <rect x="829" y="175" width="32" height="92" rx="3" fill="#e9edf3"/>
      <rect x="829" y="190" width="32" height="30" fill="#4a4e56"/>
    </g>
    <g class="address-band">
      <path d="M80,290H175L147,318L175,346H80L52,318Z" fill="var(--navy)"/>
      <path d="M66,290H80L52,318L80,346H66L38,318Z" fill="var(--bronze)"/>
      <path d="M175,290H862V346H175L203,318Z" fill="var(--bronze)"/>
      <path d="M126,305a10,10 0 0 1 20,0c0,8 -10,17 -10,17s-10,-9 -10,-17z" fill="#fff"/>
      <circle cx="136" cy="305" r="4" fill="var(--navy)"/>
    </g>
    <rect class="contact-band" x="0" y="362" width="900" height="88" fill="var(--navy)"/>
  </svg>

  <div class="brand">
    <span class="brand-name">Sam Greenfield</span>
    <span class="brand-sub">Self Storage</span>
  </div>

  <h1 class="headline"><span class="self">SELF</span> <span class="storage">STORAGE</span></h1>
  <p class="tagline">Rent Online Anytime!</p>

  <ul class="features">
    <li class="feature">
      <svg viewBox="0 0 34 34"><circle cx="17" cy="17" r="17" fill="var(--bronze)"/><path d="M9,25V13L17,8L25,13V25Z" fill="none" stroke="#fff" stroke-width="1.8"/><rect x="13" y="16" width="8" height="9" fill="none" stroke="#fff" stroke-width="1.5"/></svg>
      <span>Large/<br>Small Units</span>
    </li>
    <li class="feature">
      <svg viewBox="0 0 34 34"><circle cx="17" cy="17" r="17" fill="var(--bronze)"/><path d="M9,17L17,9L25,17V26H9Z" fill="none" stroke="#fff" stroke-width="1.8"/><line x1="17" y1="14" x2="17" y2="21" stroke="#fff" stroke-width="2"/><circle cx="17" cy="22" r="2.5" fill="#fff"/></svg>
      <span>Temperature<br>Controlled</span>
    </li>
    <li class="feature">
      <svg viewBox="0 0 34 34"><circle cx="17" cy="17" r="17" fill="var(--bronze)"/><path d="M7,14H27M8,14V23M26,14V23M10,21H24L22,24H12Z" fill="none" stroke="#fff" stroke-width="1.6"/></svg>
      <span>Covered Boat/<br>RV Parking</span>
    </li>
  </ul>

  <p class="address">217 ELMWOOD DRIVE</p>

  <p class="contact">
    <span class="phone"><svg viewBox="0 0 26 26"><path d="M6,3L10,3L12,9L9,11C10.5,14.5 12,16 15,17.5L17,14.5L23,16.5V20.5C23,22 21.5,23 20,23C11,22 4,15 3,6C3,4.5 4.5,3 6,3Z" fill="var(--bronze)"/></svg>555-201-4836</span>
    <span class="web"><svg viewBox="0 0 26 26"><g fill="none" stroke="var(--bronze)" stroke-width="1.8"><circle cx="13" cy="13" r="10"/><ellipse cx="13" cy="13" rx="4.5" ry="10"/><line x1="3" y1="13" x2="23" y2="13"/><line x1="5" y1="8" x2="21" y2="8"/><line x1="5" y1="18" x2="21" y2="18"/></g></svg>www.skylinestoragegroup.com</span>
  </p>
</main>
</body>
</html>
```